Corvell Lending Partners. Professional and Established Company

A full service finance company specializing in obtaining capital for small business. Business Lending advisor, helping small business owners access the capital they need to launch, grow, or sustain their business. Many of our programs offer flexible guidelines to overcome common obstacles such as credit score, credit history, and time in business, financials, and industry type. Our streamlined funding process makes getting a business loan, business line of credit, stated income commercial real estate loan, a smooth and stress free experience.SOME OF THE MOST COMMON NEEDS FOR BUSINESS CAPITAL:• Working Capital• Debt Consolidations (loans, merchant cash advances, etc.)• Payroll• Operating Expenses• Inventory• Equipment Financing• Commercial Real Estate (Purchase, Fix & Flip, Rehab, Renovations)• Business Acquisitions• Business ExpansionWe like the websites:www.brandtwoodfc.com they are in the same industry and provide the same servicesWe are wanting to be able to update when we do press releases and such using Word Press. Our look should be very professional and we will be adding Our Team Professional Bios and Headshots.

Industry/Entity Type

Finance

Number of Pages Required

5+ page

Font styles to use
Serif
Sans Serif

Requirements
Must have
• We want to copy brandtwoodfc.com
• We need:
• Home Page
• About Us
• Loan Programs
• Loan Criteria
• News
• Apply Now
• Contact
Nice to have
• See brandtwoodfc.com
Should not have
• Need professional design. Nothing bright or abstract

```html
<!DOCTYPE html>
<html lang="en">
<head>
<meta charset="utf-8">
<title>Corvell Lending Partners — Home</title>
<link href="https://fonts.googleapis.com/css2?family=Crimson+Text:wght@400;600&family=Lato:wght@400&display=swap" rel="stylesheet">
<style>
:root{
  --blue:#1a8cf5;
  --blue-deep:#0f7ae6;
  --cyan:#19b8f0;
  --navy:#0c1b36;
  --ink:#2a2a2a;
  --grey-text:#777;
  --panel:#f4f4f4;
  --stage:#eeeeee;
  --white:#ffffff;
  --serif:'Crimson Text', Georgia, serif;
  --sans:'Lato', Arial, sans-serif;
}
*{margin:0;padding:0;box-sizing:border-box}
html,body{width:1200px;height:1200px;overflow:hidden}
body{background:linear-gradient(90deg,#f6f6f6,#e9e9e9);font-family:var(--serif);color:var(--ink);position:relative}
.page{position:absolute;background:var(--white);overflow:hidden;box-shadow:0 4px 18px rgba(0,0,0,.18)}
.page--left{left:9px;top:34px;width:591px;height:1166px}
.page--right{left:600px;top:0;width:591px;height:1166px}
.abs{position:absolute}
.photo{position:absolute}

/* top bar + nav */
.topbar{left:0;top:0;width:591px;height:23px;background:var(--blue);color:#fff;font-family:var(--sans);font-size:6px}
.topbar span{position:absolute;top:8px}
.topbar .sq{position:absolute;left:540px;top:6px;width:10px;height:10px;background:#fff;border-radius:1px}
.nav{left:0;top:23px;width:591px;height:47px;border-bottom:1px solid #eee}
.brand{position:absolute;left:43px;top:14px;font-family:var(--serif);font-size:15px;color:#1f5fa8;font-weight:600;letter-spacing:.5px}
.menu{position:absolute;left:307px;top:20px;font-family:var(--serif);font-size:6.5px;color:#1f6fc4}
.menu span{margin-right:13px}
.menu .active{color:var(--blue)}
.underline{position:absolute;left:297px;top:43px;width:38px;height:3px;background:var(--blue)}

/* hero */
.hero{left:0;top:70px;width:591px;height:332px}
.hero-title{left:43px;top:36px;font-size:36px;line-height:34px;color:#fff}
.hero-sub{left:46px;top:114px;font-size:9px;line-height:11px;color:#fff}
.btn{left:43px;top:149px;width:90px;height:18px;border-radius:9px;background:var(--cyan);color:#fff;font-size:7px;text-align:center;line-height:18px}
.dots{left:521px;top:31px;display:flex;gap:2px}
.dot{width:5px;height:5px;border:1px solid #fff;border-radius:50%}
.dot.on{background:#fff}
.tab{left:569px;top:112px;width:22px;height:24px;background:var(--cyan);border-radius:4px 0 0 4px;color:#fff;font-size:12px;text-align:center;line-height:22px}
.closed-title{left:0;width:591px;top:204px;text-align:center;font-size:14px;color:#fff}
.loan{top:222px;width:98px;text-align:center;color:#fff;font-size:7px;line-height:11.5px}
.loan .amt{color:var(--cyan)}
.divider{top:222px;width:1px;height:84px;background:rgba(255,255,255,.45)}

/* video band */
.video{left:0;top:402px;width:591px;height:254px}
.video-box{left:213px;top:70px;width:164px;height:114px;border:1.5px solid #fff;text-align:center;color:#fff;font-size:11px;line-height:13.5px;padding-top:52px}

/* feature rows */
.feature-text{color:#fff}
.feature-text h3{font-weight:400;font-size:10.5px;margin-bottom:10px}
.feature-text p{font-size:8.2px;line-height:10.6px}
.feature-text a{color:var(--blue);text-decoration:none}

.section-title{text-align:center;font-size:16px;color:var(--blue);font-weight:400}
.program-name{font-size:22px;color:var(--blue);font-weight:400}
.program-copy{font-size:6.3px;line-height:9.2px;color:#555}

/* right column */
.arrow-circle{width:20px;height:20px;border:1px solid #444;border-radius:50%;text-align:center;line-height:17px;font-size:11px;color:#333}
.thumb{top:436px;width:32px;height:33px;box-shadow:0 1px 3px rgba(0,0,0,.25)}
.slogan{left:0;width:591px;text-align:center;color:#fff;font-size:27px;line-height:31px}
.quote-box{left:42px;top:868px;width:506px;height:102px;background:var(--panel);box-shadow:0 1px 3px rgba(0,0,0,.12)}
.quote-line{position:absolute;left:40px;width:564px;font-size:7.5px;color:#888;border-bottom:1px solid #ccc;padding-bottom:2px;width:422px}
.qmark{position:absolute;font-size:34px;color:#444;font-style:italic;font-weight:600}
.cta{left:0;top:1021px;width:591px;height:101px;background:var(--blue);color:#fff;text-align:center;font-size:20px;line-height:27px;padding-top:25px}
.footer{left:0;top:1122px;width:591px;height:44px;background:var(--blue-deep);border-top:1px solid rgba(255,255,255,.3);color:#d7ebff;font-family:var(--sans);font-size:6px;text-align:center;line-height:40px}
</style>
</head>
<body>

<!-- Home page, upper half -->
<section class="page page--left">
  <div class="abs topbar">
    <span style="left:388px">&#9990; 022 555014782</span>
    <span style="left:447px">&#9993; info@corvelllending.com</span>
    <i class="sq"></i>
  </div>
  <header class="abs nav">
    <div class="brand">Corvell Lending Partners</div>
    <nav class="menu"><span class="active">Home</span><span>About Us</span><span>Loan Programs</span><span>Loan Criteria</span><span>News</span><span>Contact</span><span>&#9906;</span></nav>
    <div class="underline"></div>
  </header>

  <div class="abs hero">
    <div class="photo" role="img" aria-label="Looking up at glass skyscrapers, tinted dark blue" style="inset:0;background:linear-gradient(135deg,#0a1730 0%,#1d3c6e 45%,#0b1a35 75%,#14294d 100%)"></div>
    <h1 class="abs hero-title" style="font-weight:400">Think<br>Exceptional</h1>
    <p class="abs hero-sub">Welcome to Corvell Lending Partners.<br>The nation's most unique private lender to<br>the commercial real estate market.</p>
    <div class="abs btn">APPLY NOW</div>
    <div class="abs dots"><i class="dot"></i><i class="dot on"></i><i class="dot"></i><i class="dot"></i></div>
    <div class="abs tab">&lt;</div>
    <h2 class="abs closed-title" style="font-weight:400">Recently Closed Loans</h2>
    <div class="abs arrow-circle" style="left:65px;top:290px;width:10px;height:10px;border-color:#fff;line-height:7px;font-size:7px;color:#fff">&lsaquo;</div>
    <div class="abs arrow-circle" style="left:539px;top:290px;width:10px;height:10px;border-color:#fff;line-height:7px;font-size:7px;color:#fff">&rsaquo;</div>
    <i class="abs divider" style="left:101px"></i><i class="abs divider" style="left:199px"></i><i class="abs divider" style="left:297px"></i><i class="abs divider" style="left:397px"></i><i class="abs divider" style="left:496px"></i>
    <div class="abs loan" style="left:102px;top:225px">Land Loan<br><span class="amt">$ 25000.000</span><br>Land Development<br>Halvorsen, jr</div>
    <div class="abs loan" style="left:200px;top:227px">Land Loan<br><span class="amt">$ 25000.000</span><br>Land Development<br>Halvorsen, jr</div>
    <div class="abs loan" style="left:299px;top:227px">Land Loan<br><span class="amt">$ 25000.000</span><br>Land Development<br>Halvorsen, jr</div>
    <div class="abs loan" style="left:398px;top:227px">Land Loan<br><span class="amt">$ 25000.000</span><br>Land Development<br>Halvorsen, jr</div>
  </div>

  <div class="abs video">
    <div class="photo" role="img" aria-label="Open-plan office with staff at desks, blue overlay" style="inset:0;background:linear-gradient(180deg,#2f8ee8 0%,#1c7fe6 55%,#2b86e0 100%)"></div>
    <div class="abs video-box">
      <svg class="abs" style="left:67px;top:14px" width="30" height="30" viewBox="0 0 30 30"><circle cx="15" cy="15" r="13" fill="none" stroke="#fff" stroke-width="1.5"/><path d="M12 9.5 L21 15 L12 20.5Z" fill="none" stroke="#fff" stroke-width="1.5" stroke-linejoin="round"/></svg>
      Watch the short video<br>of our service<br>and see how we work
    </div>
  </div>

  <div class="abs" style="left:0;top:656px;width:377px;height:164px;background:linear-gradient(135deg,#1e2530,#343c48 60%,#20262f)" role="img" aria-label="Dark city towers behind the text"></div>
  <div class="abs feature-text" style="left:43px;top:684px;width:300px">
    <h3>Bridge loans from $1 million – $70 million, as low as 6¾%</h3>
    <p>Brandtwood Capital Partners is a leading, nationwide lender to the commercial real estate market. We specialize in providing bridge loans to owners, investors and developers in need of funding outside the scope of traditional banks and lenders. <a>Read more...</a></p>
  </div>
  <div class="photo" role="img" aria-label="Industrial steel plant under a blue sky" style="left:377px;top:656px;width:214px;height:164px;background:linear-gradient(180deg,#3d7fc9 0%,#6f8fae 40%,#9a6a35 70%,#5a3e24 100%)"></div>

  <div class="photo" role="img" aria-label="Power station with chimneys by the water" style="left:0;top:820px;width:213px;height:166px;background:linear-gradient(180deg,#5a9ee0 0%,#b8cbe0 45%,#8a9099 70%,#2c5d8c 100%)"></div>
  <div class="abs" style="left:213px;top:820px;width:378px;height:166px;background:linear-gradient(135deg,#262c35,#3b434f 60%,#23282f)" role="img" aria-label="Dark city towers behind the text"></div>
  <div class="abs feature-text" style="left:239px;top:848px;width:300px">
    <h3>Bridge loans from $1 million – $70 million, as low as 6¾%</h3>
    <p>Brandtwood Capital Partners is a leading, nationwide lender to the commercial real estate market. We specialize in providing bridge loans to owners, investors and developers in need of funding outside the scope of traditional banks and lenders. <a>Read more...</a></p>
  </div>

  <h2 class="abs section-title" style="left:0;width:591px;top:1027px">Corvell Loan Programs</h2>
  <div class="photo" role="img" aria-label="Hotel facade lit at night" style="left:85px;top:1088px;width:250px;height:90px;background:linear-gradient(160deg,#1a1208,#a8721d 45%,#3a2408)"></div>
  <h3 class="abs program-name" style="left:343px;top:1128px">Hotel Loans</h3>
  <p class="abs program-copy" style="left:343px;top:1156px">We are one of a select few private lenders to</p>
</section>

<!-- Home page, lower half -->
<section class="page page--right">
  <div class="photo" role="img" aria-label="Power station with chimneys by the water" style="left:0;top:0;width:213px;height:130px;background:linear-gradient(180deg,#5a9ee0 0%,#b8cbe0 45%,#8a9099 70%,#2c5d8c 100%)"></div>
  <div class="abs" style="left:213px;top:0;width:378px;height:130px;background:linear-gradient(135deg,#262c35,#3b434f 60%,#23282f)" role="img" aria-label="Dark city towers behind the text"></div>
  <div class="abs feature-text" style="left:239px;top:-10px;width:300px">
    <h3 style="margin-bottom:5px">Bridge loans from $1 million – $70 million, as low as 6¾%</h3>
    <p>Brandtwood Capital Partners is a leading, nationwide lender to the commercial real estate market. We specialize in providing bridge loans to owners, investors and developers in need of funding outside the scope of traditional banks and lenders. <a>Read more...</a></p>
  </div>

  <h2 class="abs section-title" style="left:0;width:591px;top:171px">Corvell Loan Programs</h2>
  <div class="abs arrow-circle" style="left:43px;top:312px">&lsaquo;</div>
  <div class="abs arrow-circle" style="left:528px;top:312px">&rsaquo;</div>
  <div class="photo" role="img" aria-label="Hotel facade lit at night" style="left:86px;top:232px;width:249px;height:178px;background:linear-gradient(160deg,#1a1208,#a8721d 45%,#e0a640 55%,#3a2408)"></div>
  <h3 class="abs program-name" style="left:343px;top:270px">Hotel Loans</h3>
  <p class="abs program-copy" style="left:343px;top:299px;width:162px">We are one of a select few private lenders to specialize in land loans We are one of a select few private lenders to specialize in land loans We are one of a select few private lenders to specialize in land loans We are one of a select few private lenders to specialize in land loans We are one of a select few private lenders to specialize in land loans......</p>

  <i class="abs" style="left:210px;top:425px;width:43px;height:3px;background:var(--blue)"></i>
  <div class="photo thumb" role="img" aria-label="Office tower" style="left:88px;background:linear-gradient(#c9d3de,#6b7686)"></div>
  <div class="photo thumb" role="img" aria-label="Brick building" style="left:130px;background:linear-gradient(#9bb4cc,#8a5a3a)"></div>
  <div class="photo thumb" role="img" aria-label="Green farmland" style="left:172px;background:linear-gradient(#b8d0e6,#4f8a32)"></div>
  <div class="photo thumb" role="img" aria-label="Hotel at night" style="left:214px;width:36px;background:linear-gradient(#2a1a08,#b07a22)"></div>
  <div class="photo thumb" role="img" aria-label="Old town street" style="left:258px;background:linear-gradient(#cdb994,#6a5536)"></div>
  <div class="photo thumb" role="img" aria-label="Workshop interior" style="left:300px;background:linear-gradient(#8a8f94,#3b3f44)"></div>
  <div class="photo thumb" role="img" aria-label="City street" style="left:342px;background:linear-gradient(#4f8fd0,#2c4a6a)"></div>
  <div class="photo thumb" role="img" aria-label="Warehouse shelves" style="left:384px;background:linear-gradient(#a47a48,#5a3a1c)"></div>
  <div class="photo thumb" role="img" aria-label="Retail interior" style="left:426px;background:linear-gradient(#d8c4a4,#7a5e3e)"></div>
  <div class="photo thumb" role="img" aria-label="Family house" style="left:468px;background:linear-gradient(#e6eef6,#3f6a2c)"></div>

  <div class="abs" style="left:0;top:520px;width:591px;height:190px">
    <div class="photo" role="img" aria-label="Hand signing a document with a pen, blue overlay" style="inset:0;background:linear-gradient(120deg,#2d8ff0,#1a85ee 50%,#3994ea)"></div>
    <h2 class="abs slogan" style="top:62px;font-weight:400">It's easy to get a loan<br>unless you need it!</h2>
  </div>

  <h2 class="abs section-title" style="left:0;width:591px;top:745px">Words from Happy Clients</h2>
  <div class="photo" role="img" aria-label="Client portrait" style="left:265px;top:790px;width:60px;height:60px;border-radius:50%;background:radial-gradient(circle at 50% 45%,#c8a58a,#8a8f95 70%);border:2px solid #e8e8e8"></div>
  <div class="abs quote-box">
    <span class="qmark" style="left:40px;top:-10px">&#8220;</span>
    <p class="quote-line" style="top:22px">Lorem Ipsum Dolor Imet Lorem Ipsum Dolor Imet Lorem Ipsum Dolor Imet Lorem Ipsum Dolor Imet Lorem</p>
    <p class="quote-line" style="top:40px">Ipsum Dolor Imet Lorem Ipsum Dolor Imet Lorem Ipsum Dolor Imet Lorem Ipsum Dolor Imet Lorem.</p>
    <p class="abs" style="left:0;width:506px;top:72px;text-align:center;font-size:8px;color:#777">Daniel Marsh</p>
    <span class="qmark" style="left:456px;top:62px">&#8221;</span>
  </div>
  <div class="abs dots" style="left:284px;top:980px"><i class="dot" style="border-color:#555"></i><i class="dot on" style="border-color:#555;background:#555"></i><i class="dot" style="border-color:#555"></i><i class="dot" style="border-color:#555"></i></div>

  <div class="abs cta">take an appointment? call now<br>+022 5550147820</div>
  <footer class="abs footer">Copyright© CORVELLLENDINGPARTNERS</footer>
</section>

</body>
</html>
```